Need new sign at entrance for new fruit and vegetable wholesaler in market. Main vegetables sold are
Broccoli , Cauliflower , cabbage , capsicum , tomatoes , lettuce .
Business name is Tall Meadow
I have included examples of other designs and a sketch of suggested layout.

```html
<!DOCTYPE html>
<html lang="en">
<head>
<meta charset="utf-8">
<title>Tall Meadow – Entrance Sign</title>
<link rel="stylesheet" href="https://fonts.googleapis.com/css2?family=Alfa+Slab+One&family=Open+Sans:wght@400;600&display=swap">
<style>
  :root {
    --page-bg: #ececec;
    --sign-green-light: #e4f25a;
    --sign-green-mid: #b7d92c;
    --sign-green-deep: #8fbf1e;
    --name-ink: #1b1a17;
    --accent-red: #d9251c;
    --small-ink: #1e1e1e;
    --veg-green: #6fae3a;
    --veg-red: #d8301f;
    --veg-yellow: #f3b21a;
  }
  * { margin: 0; padding: 0; box-sizing: border-box; }
  html, body {
    width: 1200px;
    height: 1000px;
    overflow: hidden;
    background: var(--page-bg);
  }
  .canvas {
    position: relative;
    width: 1200px;
    height: 1000px;
  }
  .sign {
    position: absolute;
    left: 40px;
    top: 394px;
    width: 1120px;
    height: 212px;
    overflow: hidden;
    background:
      radial-gradient(ellipse 60% 120% at 58% 45%, var(--sign-green-light) 0%, var(--sign-green-mid) 55%, var(--sign-green-deep) 100%);
    box-shadow: 0 4px 14px rgba(0,0,0,0.18);
  }
  .stand-label {
    position: absolute;
    left: 168px;
    top: 10px;
    font-family: "Open Sans", sans-serif;
    font-weight: 600;
    font-size: 17px;
    line-height: 1.2;
    color: var(--small-ink);
  }
  .produce-art {
    position: absolute;
    left: 14px;
    top: 40px;
    width: 400px;
    height: 158px;
    border-radius: 60px 80px 50px 70px;
    background: linear-gradient(90deg,
      var(--veg-green) 0%,
      #eaf0d8 32%,
      var(--veg-green) 48%,
      var(--veg-red) 62%,
      var(--veg-yellow) 82%,
      var(--veg-green) 100%);
    opacity: 0.9;
  }
  .web-address {
    position: absolute;
    left: 436px;
    top: 52px;
    font-family: "Open Sans", sans-serif;
    font-weight: 600;
    font-size: 20px;
    line-height: 1.2;
    color: var(--accent-red);
  }
  .business-name {
    position: absolute;
    left: 430px;
    top: 82px;
    font-family: "Alfa Slab One", serif;
    font-weight: 400;
    font-size: 80px;
    line-height: 1;
    letter-spacing: -1px;
    color: var(--name-ink);
    white-space: nowrap;
  }
  .contact {
    position: absolute;
    right: 30px;
    top: 160px;
    font-family: "Open Sans", sans-serif;
    font-size: 18px;
    line-height: 1.2;
    color: var(--accent-red);
  }
  .contact-row { display: flex; justify-content: flex-end; gap: 12px; }
  .contact-label { width: 64px; text-align: right; }
</style>
</head>
<body>
  <main class="canvas">
    <section class="sign" aria-label="Tall Meadow entrance sign">
      <p class="stand-label">Stand 42 C Shed</p>
      <div class="produce-art" role="img" aria-label="Illustration of cabbage, cauliflower, lettuce, tomatoes, capsicums and broccoli"></div>
      <p class="web-address">tallmeadow.com.au</p>
      <h1 class="business-name">Tall Meadow</h1>
      <div class="contact">
        <div class="contact-row"><span class="contact-label">Phone:</span><span>02 5550 4821</span></div>
        <div class="contact-row"><span class="contact-label">Fax:</span><span>02 5550 4821</span></div>
      </div>
    </section>
  </main>
</body>
</html>
```